Web Design Project

Need a web design for a website that provides senior corporate executives with leadership assessment and improvement guidance. The homepage has two purposes- 1) place for users to log in (primary purpose), and 2) marketing of the site.

The company is named Pallor 720, and it provides 360 degree leadership assessments for senior executives. In a nutshell, that means a person's co-workers, employees, customers, and bosses fill out a survey on how well the person does his or her job; and we tell him how well he or she is doing and how to improve.

The attached logo (360_logo) should serve as the inspiration for colors, and the website must use the logo. The homepage will mostly be used for logging in, so it should be simple, clean, and professional looking. See attached sketch.pdf for what we have in mind. The sketch is provided merely to give insight. We're not married to it. All text can be latinized jibberish in the design.

There is one important size constraint to keep in mind. The attached file (content_dimensions.pdf) specifies a content area that must be (width x height) 850 x 600 px.

Note that sketch.pdf portrays images, but please note these are merely placeholders. We will use screenshots of our application on the homepage, so any images you use in content area should be examples or suggestions.
Updates

Project Deadline Extended
Reason: Looking for more submissions. Committed to payment.

Target Market(s)

Senior business executives from large companies in the manufacturing and energy sectors. Typically males aged 25 and older, white collar, upper class, with advanced degrees in business, engineering, and natural sciences.

Industry/Entity Type

It Company

Requirements
Must have
• See content_dimensions.pdf, which specifies the dimensions of the content area (850x600 px) (w x h). The the gutter and sides can expand beyond that, but the content area must be that specific size.

Note: The login panel must be within the content area.

Must use the attached logo (360_logo.png).
Should not have
• No Flash and no animated gifs. No photos of people.

```html
<!DOCTYPE html>
<html lang="en">
<head>
<meta charset="utf-8">
<title>Pallor 720 — Leadership Assessment</title>
<link rel="stylesheet" href="https://fonts.googleapis.com/css2?family=Open+Sans:ital,wght@0,400;0,600;0,700;1,400;1,700&family=Rosarivo&display=swap">
<style>
:root{
  --navy:#2f4578;
  --navy-text:#2e4373;
  --orange:#f2921d;
  --link:#1f6fc6;
  --body-text:#7a7a7a;
  --label:#777;
  --border:#cfcfcf;
  --panel:#fbfbfb;
  --button:#1f8bc6;
  --footer-text:#aab6d4;
}
*{box-sizing:border-box;margin:0;padding:0}
html,body{width:1200px;height:953px;overflow:hidden}
body{position:relative;background:#fff;font-family:"Open Sans",Arial,sans-serif;color:var(--body-text)}
.site-header{position:absolute;left:0;top:0;width:1200px;height:162px;background:linear-gradient(#f1f1f1,#fff 20%,#fff 75%,#f4f4f4)}
.brand{position:absolute;left:185px;top:48px;display:flex;align-items:center;gap:10px}
.brand-dot{width:40px;height:40px;border-radius:50%;background:var(--orange)}
.brand-name{font-size:26px;font-weight:700;color:var(--navy-text)}
.main-nav{position:absolute;left:384px;top:94px;width:388px;height:45px;display:flex;border:1px solid #c9c9c9;border-radius:4px;background:linear-gradient(#fff,#f2f2f2 55%,#e2e2e2)}
.main-nav a{flex:auto;display:flex;align-items:center;justify-content:center;font-size:15px;color:#222;text-decoration:none;border-right:1px solid #cfcfcf}
.main-nav a:last-child{border-right:0}
.call-us{position:absolute;left:885px;top:21px;display:flex;align-items:center}
.call-us svg{width:72px;height:60px}
.call-us .divider{width:1px;height:58px;background:#e2e2e2;margin:0 14px 0 10px}
.call-label{font-size:22px;font-weight:700;font-style:italic;color:var(--navy-text);line-height:1.1}
.call-number{font-size:28px;font-weight:700;color:var(--navy-text);line-height:1.05}
.search{position:absolute;left:841px;top:101px;width:259px;height:31px;border:1px solid #ddd;background:#fff;display:flex}
.search span{flex:1;font-size:13px;font-style:italic;color:#aaa;padding:6px 14px}
.search button{width:45px;border:0;border-left:1px solid #ddd;background:#fafafa;display:flex;align-items:center;justify-content:center}
.content{position:absolute;left:100px;top:162px;width:1000px;height:708px;background:var(--panel);box-shadow:inset 0 0 30px rgba(0,0,0,.05)}
.login{position:absolute;left:26px;top:36px;width:224px}
.login label{display:block;font-size:14px;color:var(--label);margin-bottom:4px}
.login .field{height:28px;border:1px solid var(--border);background:#fff;margin-bottom:15px}
.login .sign-in{display:block;width:75px;height:38px;margin-top:2px;border:0;border-radius:2px;background:var(--button);color:#fff;font:700 15px "Open Sans",sans-serif}
.categories{position:absolute;left:28px;top:262px}
.categories h2{font-size:15px;font-weight:600;color:var(--orange);width:182px;padding-bottom:6px;border-bottom:1px solid #e2e2e2;margin-bottom:10px}
.categories li{list-style:none;height:30.6px;font-size:13px;color:#777}
.categories a{color:var(--link);text-decoration:none;margin-right:8px}
.article{position:absolute;left:282px;width:690px}
.article .thumb{position:absolute;left:0;top:0;width:259px;height:165px;border:1px solid #ddd;background:#fff;padding:9px}
.article .thumb div{width:100%;height:100%}
.article h2{position:absolute;left:298px;top:-8px;font-family:"Rosarivo",Georgia,serif;font-weight:400;font-size:34px;color:var(--navy-text)}
.article p{position:absolute;left:302px;top:44px;width:390px;font-size:15px;line-height:26px}
.article .more{position:absolute;left:303px;top:134px;font-size:15px;font-weight:700;color:var(--orange);text-decoration:none}
.services{position:absolute;left:282px;top:259px;width:688px;height:165px;border:3px solid #e6e6e6;border-radius:3px;background:#fff}
.services .icon{position:absolute;left:27px;top:20px;width:118px;height:118px;border-radius:50%;background:radial-gradient(circle at 40% 35%,#bfe6fb,#3fa1e2 55%,#1d6fb5)}
.services h2{position:absolute;left:175px;top:20px;font-size:19px;font-weight:400;color:var(--navy-text)}
.services ul{position:absolute;left:177px;top:56px;display:grid;grid-template-columns:166px 166px 166px;row-gap:9px}
.services li{list-style:none;font-size:15px;color:#444;display:flex;align-items:center;gap:8px;height:22px}
.services li svg{width:11px;height:11px}
.site-footer{position:absolute;left:0;top:911px;width:1200px;height:42px;background:var(--navy)}
.site-footer p{position:absolute;left:104px;top:11px;font-size:13px;color:var(--footer-text)}
</style>
</head>
<body>
<header class="site-header">
  <div class="brand"><span class="brand-dot"></span><span class="brand-name">Pallor 720</span></div>
  <nav class="main-nav"><a href="#">About</a><a href="#">FAQ</a><a href="#">Help</a><a href="#">Contact</a></nav>
  <div class="call-us">
    <svg viewBox="0 0 72 60" aria-hidden="true">
      <path d="M6 22c0-12 60-12 60 0v6c0 3-3 4-6 4h-6c-3 0-4-2-4-5v-3c-8-3-20-3-28 0v3c0 3-1 5-4 5h-6c-3 0-6-1-6-4z" fill="#d62828"/>
      <path d="M18 30h36l8 24H10z" fill="#e03131"/>
      <circle cx="36" cy="40" r="9" fill="#fff"/>
      <circle cx="36" cy="40" r="4" fill="#c92a2a"/>
    </svg>
    <span class="divider"></span>
    <div><div class="call-label">Call Us</div><div class="call-number">555 7021</div></div>
  </div>
  <div class="search"><span>Search</span>
    <button aria-label="Search"><svg width="22" height="22" viewBox="0 0 22 22"><circle cx="13" cy="9" r="6" fill="none" stroke="#3a9fb0" stroke-width="2.5"/><path d="M9 13l-6 6" stroke="#2d6b80" stroke-width="3" stroke-linecap="round"/></svg></button>
  </div>
</header>

<main class="content">
  <form class="login">
    <label>Username</label><div class="field"></div>
    <label>Password</label><div class="field"></div>
    <button class="sign-in" type="button">Sign In</button>
  </form>

  <aside class="categories">
    <h2>Categories</h2>
    <ul>
      <li><a href="#">Reformidans</a>(5286)</li>
      <li><a href="#">Iuvaret</a>(5286)</li>
      <li><a href="#">Consequuntur</a>(5286)</li>
      <li><a href="#">Reformidans</a>(5286)</li>
      <li><a href="#">Iuvaret</a>(5286)</li>
      <li><a href="#">Consequuntur</a>(5286)</li>
      <li><a href="#">Reformidans</a>(5286)</li>
      <li><a href="#">Iuvaret</a>(5286)</li>
      <li><a href="#">Consequuntur</a>(5286)</li>
    </ul>
  </aside>

  <article class="article" style="top:34px">
    <div class="thumb"><div role="img" aria-label="Glowing blue globe with network lines" style="background:radial-gradient(circle at 60% 55%,#8fd3ff,#1673c9 55%,#062c6b)"></div></div>
    <h2>Title One Goes Here</h2>
    <p>Te vim commune accumsan, his odio laoreet eu, eu enim error assentior usu. Vidit sententiae cu usu. Eum prima dicunt expetenda ei. His cu laudem numquam</p>
    <a class="more" href="#">Read more</a>
  </article>

  <section class="services">
    <div class="icon" role="img" aria-label="Globe with a gear"></div>
    <h2>OUR SERVICES</h2>
    <ul>
      <li><svg viewBox="0 0 11 11"><circle cx="5.5" cy="5.5" r="5.5" fill="#333"/><path d="M5.5 2.5v6M2.5 5.5h6" stroke="#fff" stroke-width="1.6"/></svg>Reformidans</li>
      <li><svg viewBox="0 0 11 11"><circle cx="5.5" cy="5.5" r="5.5" fill="#333"/><path d="M5.5 2.5v6M2.5 5.5h6" stroke="#fff" stroke-width="1.6"/></svg>Reformidans</li>
      <li><svg viewBox="0 0 11 11"><circle cx="5.5" cy="5.5" r="5.5" fill="#333"/><path d="M5.5 2.5v6M2.5 5.5h6" stroke="#fff" stroke-width="1.6"/></svg>Reformidans</li>
      <li><svg viewBox="0 0 11 11"><circle cx="5.5" cy="5.5" r="5.5" fill="#333"/><path d="M5.5 2.5v6M2.5 5.5h6" stroke="#fff" stroke-width="1.6"/></svg>Iuvaret</li>
      <li><svg viewBox="0 0 11 11"><circle cx="5.5" cy="5.5" r="5.5" fill="#333"/><path d="M5.5 2.5v6M2.5 5.5h6" stroke="#fff" stroke-width="1.6"/></svg>Iuvaret</li>
      <li><svg viewBox="0 0 11 11"><circle cx="5.5" cy="5.5" r="5.5" fill="#333"/><path d="M5.5 2.5v6M2.5 5.5h6" stroke="#fff" stroke-width="1.6"/></svg>Iuvaret</li>
      <li><svg viewBox="0 0 11 11"><circle cx="5.5" cy="5.5" r="5.5" fill="#333"/><path d="M5.5 2.5v6M2.5 5.5h6" stroke="#fff" stroke-width="1.6"/></svg>Consequuntur</li>
      <li><svg viewBox="0 0 11 11"><circle cx="5.5" cy="5.5" r="5.5" fill="#333"/><path d="M5.5 2.5v6M2.5 5.5h6" stroke="#fff" stroke-width="1.6"/></svg>Consequuntur</li>
      <li><svg viewBox="0 0 11 11"><circle cx="5.5" cy="5.5" r="5.5" fill="#333"/><path d="M5.5 2.5v6M2.5 5.5h6" stroke="#fff" stroke-width="1.6"/></svg>Consequuntur</li>
    </ul>
  </section>

  <article class="article" style="top:487px">
    <div class="thumb"><div role="img" aria-label="Passenger airliner taking off under a blue sky" style="background:linear-gradient(#4a8fe0,#a9cdf2 55%,#8e9aa6 80%,#5d6a76)"></div></div>
    <h2>Title Two Goes Here</h2>
    <p>Te vim commune accumsan, his odio laoreet eu, eu enim error assentior usu. Vidit sententiae cu usu. Eum prima dicunt expetenda ei. His cu laudem numquam</p>
    <a class="more" href="#">Read more</a>
  </article>
</main>

<footer class="site-footer"><p>Copyright © Company Name &nbsp; - &nbsp; All Rights Reserved</p></footer>
</body>
</html>
```